Property Maintenance business card design

I need a business card design for my business in Adelaide , South Australia called "Cobaltline Property Maintenance and Services".
I do All kinds of property maintenance. ie
Maintenance
Repairs
Handyman services
Gardening & Landscaping
Fencing
Renovations
Cleaning & Removals
Painting
Walls & Plastering
Doors & Windows

The colours I would like are : Black and gold

I would like my business card to look as professional as possible.

If theres any more information that you may need please let me know.

Im not sure weather this image i downloaded is any good but i like the house but also the three guys, more the house i think :)

Thanks.

Target Market(s)

real estate agents and the general public looking for handy work

Industry/Entity Type

House

Contact Information for Business Card

Gordon Villeck
Mobile: 0413562708
email: cobaltlinepm@mailbox-example.com

Requirements
Nice to have
• i would like the dot points of what i do to be on the back of the card if possible, or different designs of it on the back and it not on the back.

```html
<!DOCTYPE html>
<html lang="en">
<head>
<meta charset="utf-8">
<title>Cobaltline Property Maintenance and Services – Business Card</title>
<link rel="stylesheet" href="https://fonts.googleapis.com/css2?family=Didact+Gothic&family=Questrial&display=swap">
<style>
  :root {
    --gold: #e8c21a;
    --gold-deep: #c9a20c;
    --ink: #3a3a3a;
    --ink-soft: #6b6b6b;
    --paper: #ffffff;
    --black: #000000;
    --backdrop: #8e8e8e;
  }
  * { box-sizing: border-box; margin: 0; padding: 0; }
  html, body {
    width: 1200px; height: 900px; overflow: hidden;
    background: var(--backdrop);
    font-family: "Didact Gothic", "Questrial", sans-serif;
  }
  .sheet {
    width: 1200px; height: 900px;
    display: flex; flex-direction: column; align-items: center; justify-content: center;
    gap: 40px;
  }
  .card {
    position: relative;
    width: 720px; height: 400px;
    overflow: hidden;
    box-shadow: 0 4px 14px rgba(0,0,0,0.25);
  }

  /* Front */
  .card--front { background: var(--paper); }
  .front__backdrop-art {
    position: absolute; right: 0; top: 0; width: 58%; height: 100%;
    background: radial-gradient(ellipse at 55% 45%, rgba(240,228,190,0.55), rgba(245,245,245,0.35) 55%, rgba(255,255,255,0) 80%);
  }
  .brand {
    position: absolute; left: 48px; top: 60px;
    display: flex; align-items: flex-end; gap: 16px;
  }
  .brand__mark {
    width: 58px; height: 58px; background: var(--gold);
  }
  .brand__name {
    font-family: "Questrial", sans-serif;
    font-size: 27px; line-height: 0.95; color: var(--ink);
    letter-spacing: 0.2px;
  }
  .divider {
    position: absolute; left: 0; right: 0; top: 222px;
    height: 1px; background: var(--gold);
    opacity: 0.7;
  }
  .holder {
    position: absolute; left: 48px; bottom: 58px;
    font-family: "Questrial", sans-serif;
    font-size: 40px; letter-spacing: -0.5px;
  }
  .holder__first { color: var(--gold-deep); }
  .holder__last { color: var(--ink); }
  .contact {
    position: absolute; right: 44px; top: 150px;
    text-align: right; font-size: 15px; line-height: 1.3; color: var(--ink-soft);
  }
  .contact__label { color: var(--gold-deep); margin-right: 4px; }

  /* Back */
  .card--back { background: var(--black); }
  .back__crew-art {
    position: absolute; left: 50%; top: 50%;
    width: 300px; height: 280px; transform: translate(-50%, -50%);
    background:
      linear-gradient(180deg, rgba(242,172,32,0.95) 0 12%, rgba(240,240,240,0.95) 12% 70%, rgba(90,90,90,0.45) 70% 100%);
    border-radius: 40px 40px 8px 8px;
  }
</style>
</head>
<body>
<main class="sheet">
  <section class="card card--front" aria-label="Card front">
    <div class="front__backdrop-art" role="img" aria-label="Faint illustration of three tradesmen in hard hats holding tools"></div>
    <div class="brand">
      <span class="brand__mark"></span>
      <p class="brand__name">Cobaltline<br>Property<br>Maintenance<br>&amp; Services</p>
    </div>
    <div class="divider"></div>
    <address class="contact">
      <p><span class="contact__label">Phone</span>0413562708</p>
      <p><span class="contact__label">Email</span>cobaltlinepm@mailbox-example.com</p>
    </address>
    <p class="holder"><span class="holder__first">Gordon</span><span class="holder__last">Villeck</span></p>
  </section>

  <section class="card card--back" aria-label="Card back">
    <div class="back__crew-art" role="img" aria-label="Illustration of three tradesmen in yellow hard hats holding screwdrivers, a wrench and a hammer, reflected on a glossy floor"></div>
  </section>
</main>
</body>
</html>
```